One Page Website for Personal Trainer in London

I have a logo and need a one page website designed around my branding. I am a freelance Personal Trainer based in London specialising in bodyweight training for men and women. I would like the site to be modern and clean but not overtly urban in design.
I need the following headings:
About Me
My Services
Events
Blog
I don't need them to be seperate pages but if they can link to further down the page that would be great.
Industry/Entity Type
Personal Trainer
Coding
Coded - Design and coding required
Number of Pages Required
1 page
Requirements
Must have
- I need the following headings:
- About Me
- My Services
- Events
- Blog
- mobile friendly formatting
- health and fitness related photography
- Colour scheme in keeping with my existing logo

```html
<!DOCTYPE html>
<html lang="en">
<head>
<meta charset="utf-8">
<title>Marlowe Grant – Personal Training</title>
<link rel="stylesheet" href="https://fonts.googleapis.com/css2?family=Bebas+Neue&family=Montserrat:wght@400;600;700;800&family=Open+Sans:wght@400;600&display=swap">
<style>
:root{
  --orange:#f7931e;
  --orange-dark:#e07d0c;
  --ink:#1b1b1b;
  --dark:#232323;
  --dark-2:#2e2e2e;
  --grey-text:#8a8a8a;
  --light:#ececec;
  --white:#ffffff;
}
*{box-sizing:border-box;margin:0;padding:0}
html,body{width:1200px;height:3291px;overflow:hidden}
body{position:relative;background:var(--white);font-family:"Open Sans",Arial,sans-serif;color:var(--ink)}
.abs{position:absolute}

/* top bar */
.topbar{left:0;top:0;width:1200px;height:44px;background:var(--dark)}
.topbar__mail{left:0;top:0;width:520px;height:44px;background:var(--orange);color:var(--white);font:600 15px "Montserrat",sans-serif;display:flex;align-items:center;padding-left:96px;clip-path:polygon(0 0,100% 0,96% 100%,0 100%)}
.topbar__hours{left:540px;top:0;height:44px;display:flex;align-items:center;gap:10px;color:var(--white);font:400 15px "Montserrat",sans-serif}
.social{right:38px;top:9px;display:flex;gap:8px}
.social span{width:27px;height:27px;border-radius:50%;background:var(--orange)}

/* nav */
.nav{left:0;top:44px;width:1200px;height:83px;background:var(--white);box-shadow:0 2px 6px rgba(0,0,0,.12)}
.brand{left:96px;top:60px;display:flex;align-items:center;gap:12px;font:700 28px "Montserrat",sans-serif;color:var(--ink)}
.brand__mark{width:30px;height:30px;background:var(--orange)}
.brand__sub{left:140px;top:98px;font:600 11px "Montserrat",sans-serif;letter-spacing:3px;color:var(--ink)}
.menu{right:80px;top:44px;height:83px;display:flex;align-items:center;gap:34px;font:600 13px "Montserrat",sans-serif;color:var(--ink)}

/* hero */
.hero{left:0;top:127px;width:1200px;height:564px;background:radial-gradient(ellipse at 78% 45%,#5a4a44 0%,#2a2523 35%,#0f0f0f 70%),#111}
.hero__photo{left:560px;top:127px;width:640px;height:564px;background:linear-gradient(90deg,rgba(17,17,17,0) 0%,rgba(120,90,80,.35) 45%,rgba(140,20,20,.55) 100%)}
.hero__title{left:96px;top:240px;font:400 100px/0.92 "Bebas Neue",sans-serif;color:var(--white);letter-spacing:2px}
.hero__title em{font-style:normal;color:var(--orange);display:block}
.hero__lead{left:99px;top:428px;font:400 18px "Open Sans",sans-serif;color:#ddd}
.btn{display:flex;align-items:center;justify-content:center;background:var(--orange);color:var(--white);font:700 20px "Montserrat",sans-serif;border-radius:26px}
.hero__btn{left:99px;top:498px;width:200px;height:48px}
.hero__chev{left:300px;top:505px}
.dots{left:567px;top:638px;display:flex;gap:7px}
.dots span{width:15px;height:15px;border-radius:50%;border:2px solid #999}
.dots span.on{background:var(--orange);border-color:var(--orange)}

/* side tabs */
.tab{width:86px;background:var(--white);border:3px solid #cfcfcf;border-left:none;display:flex;align-items:center;justify-content:center}
.tab span{writing-mode:vertical-rl;transform:rotate(180deg);font:600 28px "Montserrat",sans-serif}
.side-note{writing-mode:vertical-rl;transform:rotate(180deg);font:400 15px "Montserrat",sans-serif;color:#777}

/* about */
.about{left:0;top:691px;width:1200px;height:533px;background:linear-gradient(180deg,#dcdcdc,#f2f2f2 40%,#f5f5f5)}
.about__photo{left:197px;top:763px;width:327px;height:389px;border:5px solid #8e8e8e;background:linear-gradient(180deg,#8fa6b0 0%,#b7c0bd 45%,#c9b49a 100%)}
.about__label{left:555px;top:772px;width:261px;height:60px;background:var(--orange);color:var(--white);font:800 38px "Montserrat",sans-serif;display:flex;align-items:center;justify-content:center}
.about__name{left:555px;top:846px;font:800 26px "Montserrat",sans-serif}
.about__name small{font:600 15px "Open Sans",sans-serif;color:var(--grey-text);margin-left:8px}
.about__text{left:555px;top:888px;width:470px;font:400 14px/22px "Open Sans",sans-serif;color:#9a9a9a;text-align:justify}
.about__btn{left:555px;top:1108px;width:185px;height:42px;background:var(--dark-2);border-radius:21px;overflow:hidden}
.about__btn b{position:absolute;left:0;top:0;width:140px;height:42px;background:var(--orange);color:var(--white);font:700 17px "Montserrat",sans-serif;display:flex;align-items:center;justify-content:center;border-radius:21px}
.down{left:550px;top:1196px;width:100px;height:56px;border-radius:50px 50px 0 0;background:var(--white)}

/* services */
.services{left:0;top:1224px;width:1200px;height:558px;background:radial-gradient(ellipse at 50% 40%,#3a3a3a,#1d1d1d 75%)}
.section-head{left:0;width:1200px;display:flex;align-items:center;justify-content:center;gap:26px}
.section-head i{display:block;width:200px;height:4px;background:#555}
.section-head h2{font:800 38px "Montserrat",sans-serif;letter-spacing:1px}
.section-head h2 em{font-style:normal;color:var(--orange)}
.svc__icon{width:103px;height:103px;border:2px solid #4a4a4a;background:#151515;display:flex;align-items:center;justify-content:center;overflow:hidden}
.svc__icon.solid{background:var(--orange);border-color:var(--orange)}
.svc__icon::before{content:"";position:absolute;left:0;top:0;border-top:22px solid var(--orange);border-right:22px solid transparent}
.svc__title{font:700 17px "Montserrat",sans-serif;color:var(--orange)}
.svc__title span{color:var(--white)}
.svc__text{width:320px;font:400 12.5px/18px "Open Sans",sans-serif;color:#d8d8d8}

/* events */
.event__hero{left:101px;top:1935px;width:643px;height:303px;background:linear-gradient(160deg,#2c2c2c 0%,#6a6a6a 45%,#1a1a2a 100%)}
.event__caption{left:543px;top:2111px;width:201px;height:127px;background:rgba(20,20,20,.88);padding:20px 16px}
.event__caption b{display:block;font:700 17px "Montserrat",sans-serif;color:var(--orange)}
.event__caption span{display:block;font:400 12.5px/20px "Open Sans",sans-serif;color:#ccc}
.event-item{left:772px;width:318px;height:86px;background:#ececec;clip-path:polygon(0 0,88% 0,100% 50%,88% 100%,0 100%)}
.event-item__body{font:700 12.5px "Montserrat",sans-serif}
.event-item__body span{display:block;font:400 12px/20px "Open Sans",sans-serif}
.event-item__body em{display:block;font:600 12px "Open Sans",sans-serif;font-style:normal;color:var(--orange)}
.date{width:66px;height:66px;background:var(--orange);transform:rotate(45deg)}
.date__text{width:66px;text-align:center;font:700 13px/16px "Montserrat",sans-serif;color:var(--white)}

/* blog */
.blog{left:0;top:2308px;width:1200px;height:461px;background:var(--orange)}
.card__img{width:230px;height:186px;border:5px solid #d8d8d8}
.card__title{width:230px;font:800 15px/20px "Montserrat",sans-serif;color:var(--ink)}
.card__meta{font:600 11px "Montserrat",sans-serif;color:var(--ink)}

/* contact */
.contact{left:0;top:2769px;width:424px;height:445px;background:var(--white)}
.contact__title{left:0;top:2858px;width:424px;text-align:center;font:800 26px "Montserrat",sans-serif;color:var(--orange)}
.contact__title span{color:var(--ink)}
.contact__lead{left:62px;top:2913px;width:300px;text-align:center;font:400 10px/15px "Open Sans",sans-serif;color:#777}
.field{left:37px;width:349px;border:1px solid #c9c9c9;font:400 10px "Open Sans",sans-serif;color:#777;padding:7px 10px}
.contact__btn{left:134px;top:3155px;width:142px;height:33px;background:var(--orange);color:var(--white);font:700 11px "Montserrat",sans-serif;display:flex;align-items:center;justify-content:center;gap:8px}
.contact__photo{left:424px;top:2769px;width:776px;height:445px;background:radial-gradient(ellipse at 65% 50%,#6b5a52,#2a2624 55%,#121212)}
.info{left:512px;font:600 14px "Open Sans",sans-serif;color:var(--ink);display:flex;align-items:center;gap:10px}
.footer{left:0;top:3214px;width:1200px;height:77px;background:#e6e6e6;display:flex;align-items:center;justify-content:center;font:400 13px "Montserrat",sans-serif;color:#444}
</style>
</head>
<body>

<!-- top bar -->
<div class="abs topbar"></div>
<div class="abs topbar__mail">
  <svg width="18" height="18" viewBox="0 0 18 18" style="margin-right:10px"><circle cx="9" cy="9" r="9" fill="#fff"/><rect x="4" y="5.5" width="10" height="7" fill="none" stroke="#f7931e" stroke-width="1.4"/><path d="M4 5.5l5 4 5-4" fill="none" stroke="#f7931e" stroke-width="1.4"/></svg>
  Email us at hello@marlowegrant.fit
</div>
<div class="abs topbar__hours">
  <svg width="18" height="18" viewBox="0 0 18 18"><circle cx="9" cy="9" r="8" fill="none" stroke="#fff" stroke-width="1.6"/><path d="M9 4.5V9l3 2" fill="none" stroke="#fff" stroke-width="1.6"/></svg>
  Mon-Fri : 09:00am - 05:00pm
</div>
<div class="abs social"><span></span><span></span><span></span><span></span></div>

<!-- navigation -->
<header class="abs nav"></header>
<div class="abs brand"><span class="brand__mark"></span>Marlowe Grant</div>
<div class="abs brand__sub">PERSONAL TRAINING</div>
<nav class="abs menu">
  <span>HOME</span><span>ABOUT ME</span><span>MY SERVICES</span><span>EVENTS</span><span>BLOG</span><span>CONTACT US</span>
  <svg width="16" height="16" viewBox="0 0 16 16"><circle cx="6.5" cy="6.5" r="5" fill="none" stroke="#1b1b1b" stroke-width="2"/><path d="M10.5 10.5L15 15" stroke="#1b1b1b" stroke-width="2"/></svg>
</nav>

<!-- hero -->
<section class="abs hero"></section>
<div class="abs hero__photo" role="img" aria-label="Photo of a female boxer in gloves throwing a punch against a dark red backdrop"></div>
<h1 class="abs hero__title">Build Your<em>Body Strong</em></h1>
<p class="abs hero__lead">Ready to change your physique, but can't work out in the gym?</p>
<div class="abs btn hero__btn">GET STARTED</div>
<svg class="abs hero__chev" width="70" height="34" viewBox="0 0 70 34"><g fill="none" stroke="#f7931e" stroke-width="5" opacity=".9"><path d="M6 3l14 14L6 31"/><path d="M26 3l14 14-14 14" opacity=".7"/><path d="M46 3l14 14-14 14" opacity=".45"/></g></svg>
<div class="abs dots"><span class="on"></span><span></span><span></span></div>

<!-- about -->
<section class="abs about" id="about"></section>
<div class="abs tab" style="left:0;top:812px;height:259px"><span>About Me</span></div>
<div class="abs about__photo" role="img" aria-label="Photo of the trainer standing on a beach"></div>
<h2 class="abs about__label">ABOUT ME</h2>
<div class="abs about__name">TRAINER NAME<small>Freelance Personal Trainer</small></div>
<p class="abs about__text">Lorem Ipsum is simply dummy text of the printing and typesetting industry. Lorem Ipsum has been the industry's standard dummy text ever since the 1500s, when an unknown printer took a galley of type and scrambled it to make a type specimen book. It has survived not only five centuries, but also the leap into electronic typesetting, remaining essentially unchanged. It was popularised in the 1960s with the release of Inkwell sheets containing Lorem Ipsum passages, and more recently with desktop publishing software like PageSmith Studio including versions of Lorem Ipsum.</p>
<div class="abs about__btn"><b>READ MORE</b>
  <svg style="position:absolute;left:148px;top:11px" width="24" height="20" viewBox="0 0 24 20"><path d="M2 4h20M2 10h20M2 16h20" stroke="#fff" stroke-width="2"/></svg>
</div>
<div class="abs side-note" style="left:1150px;top:880px">⟵ My Services</div>

<!-- services -->
<section class="abs services" id="services"></section>
<div class="abs down"></div>
<svg class="abs" style="left:586px;top:1218px" width="28" height="18" viewBox="0 0 28 18"><path d="M3 3l11 11L25 3" fill="none" stroke="#1b1b1b" stroke-width="4"/></svg>
<svg class="abs" style="left:577px;top:1282px" width="46" height="34" viewBox="0 0 46 34"><g fill="none" stroke="#f7931e" stroke-width="4" stroke-linecap="round"><path d="M4 8h10M2 16h10M6 24h8"/><circle cx="34" cy="6" r="4" fill="#f7931e" stroke="none"/><path d="M20 14l10-4 8 8-6 8M30 10l-6 14-8 6M38 18h6"/></g></svg>
<div class="abs section-head" style="top:1316px"><i></i><h2 style="color:#fff">MY <em>SERVICES</em></h2><i></i></div>
<div class="abs side-note" style="left:30px;top:1460px;color:#999">⟵ Events</div>
<div class="abs tab" style="left:1115px;top:1371px;height:264px;width:85px;border:3px solid #cfcfcf;border-right:none;background:#1d1d1d"><span style="color:var(--orange)">My Services</span></div>

<div class="abs svc__icon solid" style="left:118px;top:1415px">
  <svg width="54" height="44" viewBox="0 0 54 44"><g fill="none" stroke="#fff" stroke-width="6" stroke-linecap="round"><path d="M8 36h38M14 30l12-14 14 14"/></g><circle cx="26" cy="8" r="6" fill="#fff"/></svg>
</div>
<div class="abs svc__title" style="left:248px;top:1417px">FITNESS <span>CLASS</span></div>
<p class="abs svc__text" style="left:248px;top:1444px">Lorem Ipsum is simply dummy text of the printing and typesetting industry. Lorem Ipsum has been the industry's standard dummy text ever since the 1500s, when an unknown printer took a galley of type and scrambled it.</p>

<div class="abs svc__icon" style="left:634px;top:1415px">
  <svg width="56" height="50" viewBox="0 0 56 50"><g fill="none" stroke="#fff" stroke-width="4"><rect x="4" y="4" width="20" height="30" rx="9"/><rect x="32" y="4" width="20" height="30" rx="9"/><path d="M7 34v10h14V34M35 34v10h14V34"/></g></svg>
</div>
<div class="abs svc__title" style="left:761px;top:1417px">BOXING <span>CLASS</span></div>
<p class="abs svc__text" style="left:761px;top:1444px">Lorem Ipsum is simply dummy text of the printing and typesetting industry. Lorem Ipsum has been the industry's standard dummy text ever since the 1500s, when an unknown printer took a galley of type and scrambled it.</p>

<div class="abs svc__icon" style="left:118px;top:1593px">
  <svg width="58" height="40" viewBox="0 0 58 40"><g fill="#fff"><rect x="2" y="12" width="6" height="16" rx="2"/><rect x="10" y="4" width="9" height="32" rx="2"/><rect x="19" y="17" width="20" height="6"/><rect x="39" y="4" width="9" height="32" rx="2"/><rect x="50" y="12" width="6" height="16" rx="2"/></g></svg>
</div>
<div class="abs svc__title" style="left:248px;top:1595px">CROSSFIT <span>CLASS</span></div>
<p class="abs svc__text" style="left:248px;top:1622px">Lorem Ipsum is simply dummy text of the printing and typesetting industry. Lorem Ipsum has been the industry's standard dummy text ever since the 1500s, when an unknown printer took a galley of type and scrambled it.</p>

<div class="abs svc__icon" style="left:634px;top:1593px">
  <svg width="50" height="56" viewBox="0 0 50 56"><g fill="none" stroke="#fff" stroke-width="4"><circle cx="25" cy="32" r="19"/><path d="M25 32V20M19 4h12M25 4v9M41 12l4-4"/></g></svg>
</div>
<div class="abs svc__title" style="left:761px;top:1595px">ENDURO <span>CLASS</span></div>
<p class="abs svc__text" style="left:761px;top:1622px">Lorem Ipsum is simply dummy text of the printing and typesetting industry. Lorem Ipsum has been the industry's standard dummy text ever since the 1500s, when an unknown printer took a galley of type and scrambled it.</p>

<!-- events -->
<svg class="abs" style="left:580px;top:1810px" width="40" height="38" viewBox="0 0 40 38"><g fill="#f7931e"><rect x="2" y="6" width="36" height="30" rx="3"/><rect x="9" y="0" width="4" height="10"/><rect x="27" y="0" width="4" height="10"/></g><g fill="#fff"><rect x="7" y="15" width="6" height="5"/><rect x="17" y="15" width="6" height="5"/><rect x="27" y="15" width="6" height="5"/><rect x="7" y="24" width="6" height="5"/><rect x="17" y="24" width="6" height="5"/></g></svg>
<div class="abs section-head" style="top:1848px" id="events"><i style="background:#e6e6e6"></i><h2>EVENTS</h2><i style="background:#e6e6e6"></i></div>
<div class="abs tab" style="left:0;top:1931px;height:252px"><span>Events</span></div>
<div class="abs side-note" style="left:1150px;top:2000px">⟵ Latest Blog</div>

<div class="abs event__hero" role="img" aria-label="Photo of a woman doing crunches on a gym mat"></div>
<svg class="abs" style="left:101px;top:2178px" width="60" height="60" viewBox="0 0 60 60"><path d="M0 0L60 60H0z" fill="#f7931e"/><path d="M20 36l-6 6 6 6" fill="none" stroke="#fff" stroke-width="3"/></svg>
<svg class="abs" style="left:700px;top:1935px" width="44" height="44" viewBox="0 0 44 44"><path d="M0 0h44v44z" fill="#f7931e"/><path d="M26 8l6 6-6 6" fill="none" stroke="#fff" stroke-width="3"/></svg>
<div class="abs event__caption"><b>POWER TRAINING</b><span>Monday January 23, 2015</span><span>6:30pm - 9:00pm / Studio A</span></div>

<div class="abs event-item" style="top:1935px"></div>
<div class="abs event-item__body" style="left:788px;top:1947px">LOREM IPSUM DOLOR SIT AMET<span>Start: 6:00pm End: 9:00pm</span><em>VIEW DETAILS ›</em></div>
<div class="abs date" style="left:1011px;top:1945px"></div>
<div class="abs date__text" style="left:1011px;top:1962px">DEC<br>10</div>

<div class="abs event-item" style="top:2043px"></div>
<div class="abs event-item__body" style="left:788px;top:2055px">LOREM IPSUM DOLOR SIT AMET<span>Start: 6:00pm End: 9:00pm</span><em>VIEW DETAILS ›</em></div>
<div class="abs date" style="left:1011px;top:2053px"></div>
<div class="abs date__text" style="left:1011px;top:2070px">DEC<br>10</div>

<div class="abs event-item" style="top:2152px"></div>
<div class="abs event-item__body" style="left:788px;top:2164px">LOREM IPSUM DOLOR SIT AMET<span>Start: 6:00pm End: 9:00pm</span><em>VIEW DETAILS ›</em></div>
<div class="abs date" style="left:1011px;top:2162px"></div>
<div class="abs date__text" style="left:1011px;top:2179px">DEC<br>10</div>

<!-- blog -->
<section class="abs blog" id="blog"></section>
<svg class="abs" style="left:584px;top:2330px" width="32" height="38" viewBox="0 0 32 38"><path d="M2 2h20l8 8v26H2z" fill="#fff"/><path d="M8 16h16M8 22h16M8 28h12" stroke="#f7931e" stroke-width="2.5"/></svg>
<div class="abs section-head" style="top:2372px"><i style="background:#e07d0c"></i><h2 style="color:#fff">LATEST <span style="color:#1b1b1b">BLOG</span></h2><i style="background:#e07d0c"></i></div>
<div class="abs side-note" style="left:30px;top:2470px;color:#1b1b1b">⟵ Contact Us</div>
<div class="abs tab" style="left:1115px;top:2413px;height:259px;width:85px;border:3px solid #fff;border-right:none;background:var(--orange)"><span style="color:#fff">Latest Blog</span></div>

<div class="abs card__img" style="left:99px;top:2451px;background:linear-gradient(180deg,#3f86c9,#9cc8ea 60%,#e7d9b8)" role="img" aria-label="Photo of a woman in a yoga pose on a beach"></div>
<div class="abs card__title" style="left:99px;top:2654px">LOREM IPSUM DOLOR SIT AMET, CONSECTETUR</div>
<div class="abs card__meta" style="left:99px;top:2710px">◷ NOV 10, 2017 &nbsp;|&nbsp; 2 COMMENTS</div>

<div class="abs card__img" style="left:360px;top:2451px;background:linear-gradient(180deg,#2a2a2a,#6e6e6e 55%,#222)" role="img" aria-label="Photo of a toned torso holding a dumbbell"></div>
<div class="abs card__title" style="left:360px;top:2654px">LOREM IPSUM DOLOR SIT AMET, CONSECTETUR</div>
<div class="abs card__meta" style="left:360px;top:2710px">◷ NOV 10, 2017 &nbsp;|&nbsp; 2 COMMENTS</div>

<div class="abs card__img" style="left:621px;top:2451px;background:linear-gradient(180deg,#8a6a4a,#a5936f 50%,#6a7a55)" role="img" aria-label="Photo of a woman doing a lunge outdoors"></div>
<div class="abs card__title" style="left:621px;top:2654px">LOREM IPSUM DOLOR SIT AMET, CONSECTETUR</div>
<div class="abs card__meta" style="left:621px;top:2710px">◷ NOV 10, 2017 &nbsp;|&nbsp; 2 COMMENTS</div>

<div class="abs card__img" style="left:869px;top:2451px;background:linear-gradient(180deg,#8fc3e4,#cfe4ef 55%,#b9a98a)" role="img" aria-label="Photo of a woman stretching by the sea"></div>
<div class="abs card__title" style="left:869px;top:2654px">LOREM IPSUM DOLOR SIT AMET, CONSECTETUR</div>
<div class="abs card__meta" style="left:869px;top:2710px">◷ NOV 10, 2017 &nbsp;|&nbsp; 2 COMMENTS</div>

<!-- contact -->
<section class="abs contact" id="contact"></section>
<div class="abs" style="left:196px;top:2805px;width:32px;height:32px;background:var(--orange)"></div>
<h2 class="abs contact__title">CONTACT <span>US</span></h2>
<p class="abs contact__lead">Lorem Ipsum is simply dummy text of the printing and typesetting industry. Lorem Ipsum has been the industry's</p>
<div class="abs field" style="top:2962px;height:35px">NAME</div>
<div class="abs field" style="top:3019px;height:35px">EMAIL</div>
<div class="abs field" style="top:3067px;height:66px">MESSAGE</div>
<div class="abs contact__btn">SEND MESSAGE
  <svg width="14" height="11" viewBox="0 0 14 11"><rect x="1" y="1" width="12" height="9" fill="none" stroke="#fff" stroke-width="1.4"/><path d="M1 1l6 5 6-5" fill="none" stroke="#fff" stroke-width="1.4"/></svg>
</div>

<div class="abs contact__photo" role="img" aria-label="Photo of a fit woman holding a dumbbell"></div>
<svg class="abs" style="left:424px;top:2769px" width="440" height="445" viewBox="0 0 440 445"><path d="M200 0L410 210 200 420 0 220V0z" fill="#fff"/><path d="M210 -10L430 210 210 430" fill="none" stroke="#e6e6e6" stroke-width="3"/></svg>
<div class="abs" style="left:590px;top:2840px;width:26px;height:26px;background:var(--orange)"></div>
<div class="abs" style="left:520px;top:2876px;font:700 24px 'Montserrat',sans-serif;color:var(--ink)">Marlowe Grant</div>
<div class="abs" style="left:548px;top:2910px;font:600 10px 'Montserrat',sans-serif;letter-spacing:3px">PERSONAL TRAINING</div>
<div class="abs info" style="top:2950px">
  <svg width="16" height="16" viewBox="0 0 16 16"><path d="M8 1a5 5 0 0 0-5 5c0 4 5 9 5 9s5-5 5-9a5 5 0 0 0-5-5z" fill="#1b1b1b"/><circle cx="8" cy="6" r="2" fill="#fff"/></svg>Address Goes Here</div>
<div class="abs info" style="top:2977px">
  <svg width="16" height="16" viewBox="0 0 16 16"><circle cx="8" cy="8" r="8" fill="#1b1b1b"/><path d="M5 4l2 2-1 1.5 2.5 2.5L10 9l2 2-1.5 1.5C7 12 4 9 3.5 5.5z" fill="#fff"/></svg>+(01) 555 - 014 - 2290</div>
<div class="abs info" style="top:3003px">
  <svg width="16" height="16" viewBox="0 0 16 16"><circle cx="8" cy="8" r="8" fill="#1b1b1b"/><rect x="4" y="5" width="8" height="6" fill="none" stroke="#fff" stroke-width="1.2"/><path d="M4 5l4 3 4-3" fill="none" stroke="#fff" stroke-width="1.2"/></svg>hello@marlowegrant.fit</div>

<footer class="abs footer">Copyright © 2017, Marlowe Grant | All Rights Reserved</footer>

</body>
</html>
```